Loft Conversion Company Website

Home page and information page design required
This is a redsign of an existing website
http://www.gablenest.example

PLATFORM
Wordpress

SERVICES
Loft Conversions
Extensions
General Building Projects

COMPETITION
Meridian Attics - meridianattics.example
Kestrel Eaves - kestreleaves.example
Dominic Harwell - dominicharwell.example

COMPANY LOGO
Take from the exiting site

COLOURS:

- Blue
- Silver
- White

STRAPLINE:
Loft Conversion Specialists

ACCREDITATIONS / LOGOS:
QTA
WPR OLV
Plover
HSD
Society of Proven Artisans
Skarn
Flue Sure

PLUGINS:
Gallery

PAGES:
Home
London Loft Conversions
- attic loft conversion
- north london loft conversions
- bungalow loft conversion
- dormer loft conversion
- loft conversions prices
- convert a loft
Technical Information
- Structural stability
- Fire safety
- Sound insulation
- Ventilation of rooms and roofs
- Sanitary facilities and drainage
- Stairs and guarding
- Thermal insulation
Gallery
- Case Studies
Testimonials
Contact Us

LOCATION(S):
London -

take correct contact info from the existing site and any pictures you wish to use

Target Market(s)

Families
Home Owners
Developers

male and female 20-65

Industry/Entity Type

Construction

Number of Pages Required

2 pages

Requirements
Must have
• Please take a look at the wireframe, the website must be very visual letting the pictures sell the product, must be classy and almost like a showroom

```html
<!DOCTYPE html>
<html lang="en">
<head>
<meta charset="utf-8">
<title>GableNest – Loft Conversion Specialists</title>
<link rel="stylesheet" href="https://fonts.googleapis.com/css2?family=Source+Sans+3:wght@400;600;700&family=Open+Sans:wght@400;600&display=swap">
<style>
:root{
  --navy:#1b2f5c;
  --navy-dark:#0f1d3e;
  --navy-text:#14264d;
  --page:#eceef1;
  --panel:#ffffff;
  --silver:#f1f1f1;
  --silver-edge:#dcdcdc;
  --grey-text:#6f6f6f;
  --body-text:#555;
  --heading-font:"Source Sans 3",sans-serif;
  --body-font:"Open Sans",sans-serif;
}
*{box-sizing:border-box;margin:0;padding:0}
html,body{width:940px;height:1200px;overflow:hidden}
body{background:var(--page);font-family:var(--body-font);position:relative;color:var(--body-text)}
.abs{position:absolute}

.site-header{left:0;top:0;width:940px;height:148px;background:linear-gradient(180deg,#1d3361 0%,#142650 100%)}
.brand-mark{left:87px;top:38px;width:50px;height:50px;background:#fff}
.brand-name{left:158px;top:76px;font-family:var(--heading-font);font-weight:600;font-size:31px;color:#fff}
.header-phone{right:85px;top:71px;font-family:var(--heading-font);font-size:16px;color:#fff;display:flex;align-items:center;gap:6px}
.strapline{right:85px;top:94px;font-family:var(--heading-font);font-size:14.5px;color:#fff}
.header-rule{left:112px;top:120px;width:744px;height:1px;background:rgba(255,255,255,.35)}
.main-nav{left:140px;top:127px;display:flex;gap:13px;font-family:var(--heading-font);font-weight:700;font-size:12px;letter-spacing:.6px;color:#fff}
.main-nav span{padding:2px 4px}
.main-nav .current{background:#fff;color:var(--navy-text);border-radius:5px}

.content-panel{left:87px;top:148px;width:768px;height:1017px;background:var(--panel)}

.services-box{left:47px;top:189px;width:343px;height:122px;background:var(--silver);box-shadow:0 1px 4px rgba(0,0,0,.18);text-align:right;padding:4px 11px 0 0;font-family:var(--heading-font);font-size:26.5px;line-height:39px;color:var(--navy-text)}

.type-list{left:275px;top:393px;font-family:var(--heading-font);font-size:13px;color:var(--grey-text)}
.type-list li{list-style:none;height:25px;padding:0 7px}
.type-list .active{background:var(--silver);color:#333;border-radius:3px;box-shadow:0 1px 2px rgba(0,0,0,.2);width:130px}

.hero-frame{left:412px;top:189px;width:418px;height:326px;background:var(--silver);box-shadow:0 1px 3px rgba(0,0,0,.18)}
.hero-photo{left:10px;top:9px;width:398px;height:302px;background:linear-gradient(180deg,#f4f4f2 0%,#f4f4f2 22%,#9a4a38 35%,#a8584a 55%,#b9b5b0 75%,#8e4434 100%)}
.hero-dots{right:10px;bottom:4px;display:flex;gap:6px}
.hero-dots i{width:5px;height:5px;border-radius:50%;background:#aaa}
.hero-dots i:first-child{background:#444}

.accreditations{left:47px;top:549px;width:846px;height:59px;background:var(--silver);box-shadow:0 1px 4px rgba(0,0,0,.18);display:flex;justify-content:center;align-items:center;gap:22px}
.badge{background:#c8cdd6;border-radius:4px}

.column-title{top:644px;font-family:var(--heading-font);font-weight:600;font-size:15.5px;color:var(--navy-text);text-align:center;width:240px}
.column-rule{top:640px;width:1px;height:280px;background:linear-gradient(180deg,transparent,#e2e2e2,transparent)}

.testimonial-photo{left:129px;width:56px;height:65px;border:1px solid #888;background:#fafbfd}
.testimonial-quote{left:199px;width:138px;font-size:10.8px;line-height:13px;color:var(--body-text)}
.testimonial-name{font-family:var(--heading-font);font-weight:600;font-size:12px;color:#222;text-align:right;width:135px;left:199px}
.scroll-btn{left:104px;width:15px;height:15px;border:1px solid #bbb;border-radius:50%;display:flex;align-items:center;justify-content:center}

.guarantee-text{left:373px;top:686px;width:210px;font-size:10.9px;line-height:13.1px;color:var(--body-text)}
.read-more{left:513px;top:888px;font-family:var(--heading-font);font-size:12px;color:var(--navy-text)}

.field{left:617px;width:139px;height:22px;background:#f4f4f4;border:1px solid #d6d6d6;font-style:italic;font-size:9.5px;color:#888;padding:5px 8px}
.field-comments{width:202px;height:70px}
.form-btn{top:884px;height:18px;background:var(--navy-dark);color:#fff;font-family:var(--heading-font);font-size:10.5px;display:flex;align-items:center;justify-content:center;border-radius:2px}

.feature-box{top:956px;width:230px;height:182px;background:linear-gradient(180deg,#284678 0%,#1b3262 60%,#142852 100%);border-radius:4px}
.feature-title{left:11px;top:10px;font-family:var(--heading-font);font-size:16.5px;color:#fff;display:flex;align-items:center;gap:8px}
.showroom-photo{left:24px;top:48px;width:183px;height:87px;background:linear-gradient(90deg,#5b4d4a 0%,#e5e3e0 45%,#c63a3a 75%,#dcdad6 100%)}
.carousel-btn{top:79px;width:25px;height:25px;border-radius:50%;background:var(--navy-dark);border:3px solid #fff;color:#fff;font-size:11px;display:flex;align-items:center;justify-content:center}
.van-photo{left:20px;top:42px;width:190px;height:128px;background:radial-gradient(ellipse at center,#e8ebef 0%,#b8bfc9 40%,rgba(27,50,98,0) 72%)}
.contact-list{left:14px;top:44px;font-family:var(--heading-font);font-size:11.5px;color:#fff;line-height:13px}
.contact-list dt{position:absolute;left:0}
.contact-list dd{margin-left:58px;margin-bottom:13px}

.site-footer{top:1172px;font-size:9.5px;color:#888}
</style>
</head>
<body>

<header class="site-header abs">
  <div class="brand-mark abs"></div>
  <div class="brand-name abs">GableNest</div>
  <div class="header-phone abs">
    <svg width="14" height="18" viewBox="0 0 14 18"><path d="M3 1c1 0 2 3 2 4s-2 1-2 2 2 5 3 5 1-2 2-2 3 2 3 3-2 3-3 3C5 16 1 9 1 4 1 2 2 1 3 1z" fill="#fff"/></svg>
    020 7946 0321
  </div>
  <div class="strapline abs">Loft Conversion Specialists</div>
  <div class="header-rule abs"></div>
  <nav class="main-nav abs">
    <span class="current">HOME</span><span>LONDON LOFT CONVERSIONS</span><span>TECHNICAL INFORMATION</span><span>GALLERY</span><span>TESTIMONIALS</span><span>CONTACT US</span>
  </nav>
</header>

<main>
  <div class="content-panel abs"></div>

  <div class="services-box abs">Loft Conversions<br>Extensions<br>General Building Projects</div>

  <ul class="type-list abs">
    <li>Terraced House</li>
    <li>Detached House</li>
    <li>Office Conversion</li>
    <li>Bungalow Conversion</li>
    <li class="active">Skarn Conversion</li>
  </ul>

  <div class="hero-frame abs">
    <div class="hero-photo abs" role="img" aria-label="Red brick house with tiled roof, roof windows and white bay window"></div>
    <div class="hero-dots abs"><i></i><i></i><i></i><i></i><i></i></div>
  </div>

  <section class="accreditations abs" aria-label="Accreditations">
    <div class="badge" style="width:24px;height:36px;border-radius:12px 12px 3px 3px"></div>
    <div class="badge" style="width:64px;height:30px"></div>
    <div class="badge" style="width:30px;height:34px;border-radius:4px 4px 15px 15px"></div>
    <div class="badge" style="width:22px;height:36px"></div>
    <div class="badge" style="width:34px;height:34px;border-radius:50%"></div>
    <div class="badge" style="width:34px;height:34px;border-radius:50%"></div>
    <div class="badge" style="width:60px;height:20px;border-radius:2px"></div>
  </section>

  <h2 class="column-title abs" style="left:100px">Visit our clients homes</h2>
  <h2 class="column-title abs" style="left:347px">10 Year Guarantee</h2>
  <h2 class="column-title abs" style="left:596px">Free Survey</h2>
  <div class="column-rule abs" style="left:352px"></div>
  <div class="column-rule abs" style="left:595px"></div>

  <div class="testimonial-photo abs" style="top:694px"></div>
  <p class="testimonial-quote abs" style="top:693px">‘I would like to thank you for the excellent standard of service and work when completing our attic loft conversion last year.’</p>
  <p class="testimonial-name abs" style="top:767px">Mathis, Enfield</p>
  <div class="scroll-btn abs" style="top:760px"><svg width="7" height="5"><path d="M0.5 4.5L3.5 0.8 6.5 4.5" fill="none" stroke="#888"/></svg></div>
  <div class="scroll-btn abs" style="top:788px"><svg width="7" height="5"><path d="M0.5 0.5L3.5 4.2 6.5 0.5" fill="none" stroke="#888"/></svg></div>
  <div class="testimonial-photo abs" style="top:802px"></div>
  <p class="testimonial-quote abs" style="top:801px">I could not be more pleased with the way my attic loft conversion has been finished the quality of work is absolutely fantastic.’</p>
  <p class="testimonial-name abs" style="top:888px">Owen, Enfield</p>

  <p class="guarantee-text abs">Lorem ipsum dolor sit amet, consectetur adipiscing elit. Ut non sapien dolor.Morbi tempus nisi non leo ullamcorper non feugiat turpis fringilla. Nunc commodo aliquet tellus eget placerat. Suspendisse et dui et sem adipiscing rhoncus. Nunc ullamcorper, eros vel gravida tristique, orci nibh vulputate justo, eleifend porttitor elit lacus in neque. Praesent pretium nibh in velit venenatis convallis. Praesent pretium commodo mauris gravida viverra.Curabitur ornare ullamcorper elit sit amet.Donec ac erat non nibh rutrum egestas nec a turpis.</p>
  <a class="read-more abs">Read more &gt;&gt;</a>

  <form aria-label="Free survey">
    <div class="field abs" style="top:688px">Name</div>
    <div class="field abs" style="top:720px">Email</div>
    <div class="field abs" style="top:753px">Telephone</div>
    <div class="field field-comments abs" style="top:795px">Comments</div>
    <div class="form-btn abs" style="left:713px;width:45px">RESET</div>
    <div class="form-btn abs" style="left:764px;width:55px">SUBMIT</div>
  </form>

  <section class="feature-box abs" style="left:105px">
    <h3 class="feature-title abs">Visit our showroom</h3>
    <div class="showroom-photo abs" role="img" aria-label="Finished loft bedroom with double bed and red cushions"></div>
    <div class="carousel-btn abs" style="left:-12px">&lt;</div>
    <div class="carousel-btn abs" style="left:217px">&gt;</div>
  </section>

  <section class="feature-box abs" style="left:355px">
    <h3 class="feature-title abs" style="left:17px">Unrivelled After Support</h3>
    <div class="van-photo abs" role="img" aria-label="Fleet of white company vans"></div>
  </section>

  <section class="feature-box abs" style="left:606px">
    <h3 class="feature-title abs" style="left:14px">
      <svg width="17" height="12" viewBox="0 0 17 12"><rect x="0.5" y="0.5" width="16" height="11" fill="#fff"/><path d="M0.5 0.5l8 6 8-6" fill="none" stroke="#9aa8c0"/></svg>
      Contact Us
    </h3>
    <dl class="contact-list abs">
      <dt>Tel:</dt><dd>020 7946 0321</dd>
      <dt>Address:</dt><dd>GableNest<br>18 Linden Row<br>Enfield<br>Middlesex<br>EN2 7QX</dd>
      <dt>Email:</dt><dd>sales@gablenest.example<br>aftersales@gablenest.example</dd>
    </dl>
  </section>
</main>

<footer>
  <p class="site-footer abs" style="left:87px">Copyright 2010 GableNest. All rights reserved.</p>
  <p class="site-footer abs" style="right:84px">Home / London Loft Conversions / Technical Information / Gallery / Testimonials / Contact</p>
</footer>

</body>
</html>
```